New Business Card Design Project

Harbor of the Willow Wellness Clinic PLLC
Harborofthewillowwc.example
Board Certified Nursing Coach in life, health, & wellness.
Hypnotherapy, weight loss & vitamin supplement injections, IV hydration.
Offering mobile clinics

```html
<!DOCTYPE html>
<html lang="en">
<head>
<meta charset="utf-8">
<title>Harbor of the Willow Wellness Clinic – Business Card</title>
<link rel="stylesheet" href="https://fonts.googleapis.com/css2?family=Arimo:wght@400;700&display=swap">
<style>
  :root{
    --stage:#3b3b3b;
    --maroon:#553032;
    --maroon-deep:#45262a;
    --umber:#3a2a20;
    --umber-light:#5c4431;
    --flame:#e9823a;
    --flame-red:#d8352a;
    --ink:#ffffff;
    --ink-soft:#e6d9d6;
  }
  *{box-sizing:border-box;margin:0;padding:0}
  html,body{width:1200px;height:803px;overflow:hidden;background:var(--stage)}
  body{position:relative;font-family:"Arimo",Arial,sans-serif;color:var(--ink)}

  .card{position:absolute;top:252px;width:520px;height:298px;border-radius:18px;
        overflow:hidden;border:1.5px solid var(--flame);
        box-shadow:0 14px 30px rgba(0,0,0,.45)}
  .card--contact{left:50px;background:linear-gradient(135deg,var(--umber-light),var(--umber))}
  .card--front{left:630px;background:var(--maroon)}

  .artwork{position:absolute;right:0;top:0;width:300px;height:298px;
           background:radial-gradient(circle at 58% 42%,#f4e3c8 0 14%,#ef9a45 26%,#c8622a 42%,rgba(90,64,45,0) 70%)}

  .contact-shape{position:absolute;inset:0;width:100%;height:100%}

  .wordmark{font-weight:700;color:var(--ink);text-transform:uppercase;white-space:nowrap}

  .contact-panel{position:absolute;left:34px;top:36px;width:300px}
  .contact-panel .wordmark{font-size:17px;letter-spacing:2.5px;line-height:1.25}
  .contact-panel .wordmark small{display:block;font-size:9px;letter-spacing:3px}
  .person-name{margin-top:20px;font-size:22px;font-weight:700}
  .person-title{font-size:12px;color:var(--ink-soft);margin-top:2px}
  .address{margin-top:14px;font-size:12px;line-height:1.35}
  .contact-list{list-style:none;margin-top:12px;font-size:12px;line-height:1.55}
  .contact-list li{display:flex;align-items:center;gap:8px}
  .contact-list svg{width:11px;height:11px;flex:none}

  .front-brand{position:absolute;left:28px;right:28px;top:98px;display:flex;align-items:center;justify-content:center;gap:14px}
  .brand-dot{width:40px;height:40px;border-radius:50%;background:var(--flame);flex:none}
  .front-brand .wordmark{font-size:22px;letter-spacing:2.5px;line-height:1.1}
  .front-brand .wordmark small{display:flex;align-items:center;justify-content:center;gap:10px;font-size:11px;letter-spacing:3px;margin-top:7px}
  .rule{display:inline-block;width:40px;height:1.5px;background:var(--ink)}
  .tagline{position:absolute;left:30px;right:30px;bottom:56px;text-align:center;font-size:13px;line-height:1.35;color:var(--ink-soft)}
</style>
</head>
<body>

<section class="card card--contact" aria-label="Business card, contact side">
  <div class="artwork" role="img" aria-label="Phoenix illustration in glowing orange flame tones"></div>
  <svg class="contact-shape" viewBox="0 0 520 298" aria-hidden="true">
    <defs>
      <linearGradient id="edgeGlow" x1="0" y1="0" x2="1" y2="1">
        <stop offset="0" stop-color="#e9823a"/>
        <stop offset="1" stop-color="#d8352a"/>
      </linearGradient>
    </defs>
    <circle cx="40" cy="330" r="352" fill="url(#edgeGlow)"/>
    <circle cx="34" cy="334" r="344" fill="#553032"/>
  </svg>

  <div class="contact-panel">
    <p class="wordmark">Harbor of the Willow<small>Wellness Clinic</small></p>
    <p class="person-name">Dana Merrow</p>
    <p class="person-title">President</p>
    <p class="address">412 Alder Bend Road<br>Juneau, AK 99801</p>
    <ul class="contact-list">
      <li><svg viewBox="0 0 12 12"><path d="M2.5 1h2l1 3-1.3 1a6 6 0 0 0 2.8 2.8L8 6.5l3 1v2A1.5 1.5 0 0 1 9.5 11 8.5 8.5 0 0 1 1 2.5 1.5 1.5 0 0 1 2.5 1z" fill="#fff"/></svg>555-014-2273</li>
      <li><svg viewBox="0 0 12 12"><rect x="3" y="0.8" width="6" height="10.4" rx="1" fill="none" stroke="#fff" stroke-width="1.2"/><circle cx="6" cy="9.3" r=".7" fill="#fff"/></svg>555-019-3866</li>
      <li><svg viewBox="0 0 12 12"><rect x="1" y="2.5" width="10" height="7" rx="1" fill="#fff"/><path d="M1.5 3l4.5 3.5L10.5 3" fill="none" stroke="#553032" stroke-width="1"/></svg>hello@harborofthewillowwc.example</li>
      <li><svg viewBox="0 0 12 12"><circle cx="6" cy="6" r="5" fill="none" stroke="#fff" stroke-width="1.1"/><path d="M1 6h10M6 1c-2.5 3-2.5 7 0 10M6 1c2.5 3 2.5 7 0 10" fill="none" stroke="#fff" stroke-width=".9"/></svg>Harborofthewillowwc.example</li>
    </ul>
  </div>
</section>

<section class="card card--front" aria-label="Business card, front side">
  <div class="front-brand">
    <span class="brand-dot" aria-hidden="true"></span>
    <p class="wordmark">Harbor of the Willow
      <small><span class="rule"></span>Wellness Clinic<span class="rule"></span></small>
    </p>
  </div>
  <p class="tagline">Hypnotherapy, weight loss &amp; vitamin supplement injections<br>IV hydration. Offering mobile clinics</p>
</section>

</body>
</html>
```